Wine Label Design

Organization name: Orvell Wine Company

My company is called Orvell Wine Company, I’m a wine importer and wholesaler who distributes wine domestically.

We are about to launch a line of three premium and one sparkling wine that we will wholesale to various retailers, wine stores, and restaurants for re-sale. The wines label will have “Dean Marlowe” I plan on having the labels the same and just changing the varietal as needed. My wine are made from premium grapes and will be marketed as a high end wine. My current label size is 3 1/2" wide by 5" in long and the labels can be on a solid background or transparent.

I would like the first label to be for my Cabernet Sauvignon, California, 2012, 750ML (for the size of the bottle) and ALC 13.8% BY VOL (for the alcohol content).

Colors: I am open to any and all designs that would alter my perception of what will be best!

Further:
Current label is boring and poorly done, so hopefully you designers can come up with something better

Industry/Entity Type

It Company

```html
<!DOCTYPE html>
<html lang="en">
<head>
<meta charset="utf-8">
<title>Dean Marlowe – Cabernet Sauvignon Labels</title>
<link rel="stylesheet" href="https://fonts.googleapis.com/css2?family=Parisienne&family=Great+Vibes&family=Cinzel:wght@700&family=Lato:wght@400&display=swap">
<style>
  :root {
    --canvas: #ffffff;
    --gold: #c9a865;
    --gold-light: #f3e2a8;
    --gold-dark: #9c7a3c;
    --white: #ffffff;
    --red: #851a22;
    --red-deep: #4a0c12;
    --teal: #216a78;
    --teal-deep: #0f3a44;
    --purple: #5b2169;
    --purple-deep: #2c0d35;
  }
  * { margin: 0; padding: 0; box-sizing: border-box; }
  html, body {
    width: 1200px; height: 594px; overflow: hidden;
    background: var(--canvas);
  }
  .label-row { position: relative; width: 1200px; height: 594px; }
  .label {
    position: absolute; top: 57px; width: 335px; height: 478px;
    background: var(--base); overflow: hidden;
    text-align: center;
  }
  .label--red { left: 50px; --base: var(--red); --deep: var(--red-deep); }
  .label--teal { left: 433px; --base: var(--teal); --deep: var(--teal-deep); }
  .label--purple { left: 817px; --base: var(--purple); --deep: var(--purple-deep); }

  .gold-band {
    position: absolute; left: 0; width: 100%; height: 8px;
    background: linear-gradient(90deg, var(--gold-dark), var(--gold-light) 30%, var(--gold) 60%, var(--gold-light) 85%, var(--gold-dark));
    z-index: 3;
  }
  .gold-band--top { top: 0; }
  .gold-band--bottom { bottom: 0; }

  .scrollwork { position: absolute; z-index: 1; }
  .scrollwork--top-left {
    top: 0; left: 0; width: 120px; height: 150px;
    background: radial-gradient(ellipse at top left, var(--deep) 0%, transparent 70%);
  }
  .scrollwork--top-right {
    top: 0; right: 0; width: 80px; height: 120px;
    background: radial-gradient(ellipse at top right, var(--deep) 0%, transparent 70%);
  }
  .scrollwork--bottom-left {
    bottom: 0; left: 0; width: 110px; height: 140px;
    background: radial-gradient(ellipse at bottom left, var(--deep) 0%, transparent 70%);
  }
  .scrollwork--bottom-right {
    bottom: 0; right: 0; width: 150px; height: 200px;
    background: radial-gradient(ellipse at bottom right, var(--deep) 0%, transparent 72%);
  }

  .divider {
    position: absolute; left: 57px; width: 221px; height: 12px;
    background: var(--deep); opacity: .75; border-radius: 6px; z-index: 2;
  }
  .divider--upper { top: 147px; }
  .divider--lower { top: 347px; }

  .text { position: absolute; left: 0; width: 100%; z-index: 2; line-height: 1; }
  .brand {
    top: 72px; font-family: "Parisienne", cursive;
    font-size: 50px; color: var(--gold);
  }
  .varietal {
    top: 172px; font-family: "Cinzel", serif; font-weight: 700;
    font-size: 39px; line-height: 47px; color: var(--gold);
    letter-spacing: .5px;
  }
  .region {
    top: 270px; font-family: "Great Vibes", cursive;
    font-size: 28px; color: var(--white);
  }
  .vintage {
    position: absolute; top: 312px; left: 129px; width: 77px; height: 30px;
    border-radius: 50%; background: var(--deep); z-index: 2;
    font-family: "Lato", sans-serif; font-size: 19px; color: var(--gold);
    line-height: 30px;
  }
  .volume {
    top: 397px; font-family: "Lato", sans-serif;
    font-size: 15px; color: var(--white);
  }
  .alcohol {
    top: 428px; font-family: "Lato", sans-serif;
    font-size: 11.5px; color: var(--white);
  }
</style>
</head>
<body>
<main class="label-row">

  <section class="label label--red">
    <div class="gold-band gold-band--top"></div>
    <div class="scrollwork scrollwork--top-left" role="img" aria-label="Baroque floral scrollwork"></div>
    <div class="scrollwork scrollwork--top-right" role="img" aria-label="Baroque floral scrollwork"></div>
    <div class="scrollwork scrollwork--bottom-left" role="img" aria-label="Baroque floral scrollwork"></div>
    <div class="scrollwork scrollwork--bottom-right" role="img" aria-label="Baroque floral scrollwork"></div>
    <p class="text brand">Dean Marlowe</p>
    <div class="divider divider--upper" role="img" aria-label="Ornamental scroll divider"></div>
    <h1 class="text varietal">Cabernet<br>Sauvignon</h1>
    <p class="text region">California</p>
    <p class="vintage">2012</p>
    <div class="divider divider--lower" role="img" aria-label="Ornamental scroll divider"></div>
    <p class="text volume">750 ML</p>
    <p class="text alcohol">ALC 13.8% BY VOL</p>
    <div class="gold-band gold-band--bottom"></div>
  </section>

  <section class="label label--teal">
    <div class="gold-band gold-band--top"></div>
    <div class="scrollwork scrollwork--top-left" role="img" aria-label="Baroque floral scrollwork"></div>
    <div class="scrollwork scrollwork--top-right" role="img" aria-label="Baroque floral scrollwork"></div>
    <div class="scrollwork scrollwork--bottom-left" role="img" aria-label="Baroque floral scrollwork"></div>
    <div class="scrollwork scrollwork--bottom-right" role="img" aria-label="Baroque floral scrollwork"></div>
    <p class="text brand">Dean Marlowe</p>
    <div class="divider divider--upper" role="img" aria-label="Ornamental scroll divider"></div>
    <h1 class="text varietal">Cabernet<br>Sauvignon</h1>
    <p class="text region">California</p>
    <p class="vintage">2012</p>
    <div class="divider divider--lower" role="img" aria-label="Ornamental scroll divider"></div>
    <p class="text volume">750 ML</p>
    <p class="text alcohol">ALC 13.8% BY VOL</p>
    <div class="gold-band gold-band--bottom"></div>
  </section>

  <section class="label label--purple">
    <div class="gold-band gold-band--top"></div>
    <div class="scrollwork scrollwork--top-left" role="img" aria-label="Baroque floral scrollwork"></div>
    <div class="scrollwork scrollwork--top-right" role="img" aria-label="Baroque floral scrollwork"></div>
    <div class="scrollwork scrollwork--bottom-left" role="img" aria-label="Baroque floral scrollwork"></div>
    <div class="scrollwork scrollwork--bottom-right" role="img" aria-label="Baroque floral scrollwork"></div>
    <p class="text brand">Dean Marlowe</p>
    <div class="divider divider--upper" role="img" aria-label="Ornamental scroll divider"></div>
    <h1 class="text varietal">Cabernet<br>Sauvignon</h1>
    <p class="text region">California</p>
    <p class="vintage">2012</p>
    <div class="divider divider--lower" role="img" aria-label="Ornamental scroll divider"></div>
    <p class="text volume">750 ML</p>
    <p class="text alcohol">ALC 13.8% BY VOL</p>
    <div class="gold-band gold-band--bottom"></div>
  </section>

</main>
</body>
</html>
```